Briefkopf und Visitenkarte für Kanzlei
Zielgruppe
Wir sind eine Kanzlei mit Sitz in Neuss und den Schwerpunkten im Arbeitsrecht und Strafrecht. Unser Rechtsanwalt Kerem Albayrak ist zugleich Fachanwalt für das Arbeitsrecht. Unsere Zielgruppe sind alle Menschen, die in diesen beiden Gebieten Rechtsberatung oder Vertretung suchen. Nähere Informationen über uns findet Ihr auf www.hovenrat-kanzlei.de
Aufgabenstellung
Was ich möchte:
- das Design sollte schlicht sein und nicht zu dick auftragen. Zu schlicht ist aber auch nicht gut, schlielich soll erkennbar sein, dass die Briefvorlage nicht von einem Laien ertellt wurde, sondern von einem Designer.
- Farbakzente wie marineblau und gold sind gewünscht, allerdings nicht zu übertrieben, weil das sonst vom Textinhalt ablenkt und zu viel Tinte verbraucht.
- Der Briefkopf sollte folgende Informationen anzeigen: Fachanwaltstitel, Anschrift, Kontaktmöglichkeiten wie Telefon, Fax, E-Mail und Webseite, Öffnungszeiten, Bankverbindung und Umsatzsteuer IDNr.
- Eine Kopfzeile oder Fußzeile mit dem Kanzleinamen - / Logo, die auch ab Seite 1. weitergeführt wird.
- Die Seitenzahl sollte ersichtlich sein.
- Die Endddatei sollte hinsichtlich der angegebenen Daten (wie bspw. Telefonnummer und Anschrift) leicht veränderbar sein (gewünscht sind word und rtf als Dateiformat)
- Die Schriftart für den Schriftzug Halls Of Falcons ist Trajan pro.
Was ich nicht möchte:
- Keine Wasserzeichen in der Mitte des Textes. Das lenkt von der Schrift ab.
- Die Enddatei sollte nicht groß sein (idealerweise unter 0,75 -1 mb), da wir unsere Schreiben oft per Mail versenden und der Anhang dadurch zu groß würde.

```html
<!DOCTYPE html>
<html lang="de">
<head>
<meta charset="utf-8">
<title>Briefkopf – Kerem Albayrak, Fachanwalt für Arbeitsrecht</title>
<link rel="stylesheet" href="https://fonts.googleapis.com/css2?family=Cinzel:wght@400;500&family=Arimo:wght@400&family=Tinos&display=swap">
<style>
  :root {
    --navy: #2a3a7c;
    --navy-dark: #28326f;
    --gold: #a08a5a;
    --gold-light: #e8d9a0;
    --gold-mid: #c9a95a;
    --ink: #2b2b2b;
    --paper: #ffffff;
    --rule: #c8c8c8;
  }
  html, body { margin: 0; padding: 0; overflow: hidden; background: var(--paper); }
  .letterhead {
    position: relative;
    width: 849px;
    height: 1200px;
    background: var(--paper);
    overflow: hidden;
    font-family: "Arimo", Arial, sans-serif;
    color: var(--ink);
  }
  .top-band {
    position: absolute; left: 0; top: 0; width: 100%; height: 13px;
    background: linear-gradient(90deg, #b89c5c 0%, #efe2a8 30%, #cdb06a 50%, #b8953e 72%, #efe2a8 88%, #c6a862 100%);
  }
  .bottom-band {
    position: absolute; left: 0; top: 1186px; width: 100%; height: 13px;
    background: var(--navy-dark);
  }
  .brand-mark {
    position: absolute; left: 383px; top: 28px; width: 82px; height: 82px; border-radius: 50%;
    background: radial-gradient(circle at 40% 35%, var(--gold-light), var(--gold-mid) 60%, #a8883e 100%);
  }
  .brand-name {
    position: absolute; left: 0; width: 849px; top: 112px; text-align: center;
    font-family: "Cinzel", serif; font-size: 32px; color: var(--navy); letter-spacing: 1px; line-height: 1;
  }
  .brand-title {
    position: absolute; left: 0; width: 849px; top: 147px; text-align: center;
    font-size: 11px; color: var(--gold); letter-spacing: 0.2px;
  }
  .sender-line {
    position: absolute; left: 135px; top: 198px; font-size: 10.5px; color: var(--ink);
  }
  .sender-line .dot, .contact-address .dot { color: var(--navy); }
  .sidebar {
    position: absolute; left: 623px; top: 168px; width: 220px; font-size: 11px; line-height: 16.5px;
  }
  .contact-name { font-size: 16px; letter-spacing: 1.6px; line-height: 1; margin: 0 0 8px; font-weight: 400; }
  .contact-address { font-size: 13px; margin: 0 0 10px; line-height: 1; }
  .sidebar h3 { font-size: 11px; font-weight: 400; color: var(--navy); margin: 0; line-height: 16.5px; }
  .sidebar p { margin: 0; }
  .sidebar .block { margin-bottom: 13px; }
  .label { color: var(--navy); display: inline-block; }
  .label.tel, .label.fax { width: 38px; }
  .label.web { width: 38px; }
  .fold-mark { position: absolute; height: 1px; background: var(--rule); }
  .fold-top { left: 18px; top: 402px; width: 21px; }
  .fold-punch { left: 26px; top: 598px; width: 38px; }
  .fold-bottom { left: 18px; top: 804px; width: 21px; }
  .footer-mark {
    position: absolute; left: 397px; top: 1063px; width: 54px; height: 54px; border-radius: 50%;
    background: radial-gradient(circle at 40% 35%, var(--gold-light), var(--gold-mid) 60%, #a8883e 100%);
  }
  .footer-name {
    position: absolute; left: 0; width: 849px; top: 1124px; text-align: center;
    font-family: "Cinzel", serif; font-size: 24px; color: var(--navy); line-height: 1; letter-spacing: 0.5px;
  }
  .footer-sub {
    position: absolute; left: 0; width: 849px; top: 1155px; text-align: center;
    font-size: 11px; letter-spacing: 6.3px; color: var(--ink);
  }
  .page-number {
    position: absolute; left: 75px; top: 1131px; font-family: "Tinos", serif; font-size: 20px; color: var(--ink);
  }
</style>
</head>
<body>
<main class="letterhead">
  <div class="top-band"></div>

  <header class="brand">
    <div class="brand-mark"></div>
    <div class="brand-name">ALBAYRAK</div>
    <div class="brand-title">FACHANWALT FÜR ARBEITSRECHT</div>
  </header>

  <div class="sender-line">RA Kerem Albayrak <span class="dot">•</span>&nbsp; Lindenallee 22 <span class="dot">•</span> 41460 Neuss</div>

  <aside class="sidebar">
    <h2 class="contact-name">Kerem Albayrak</h2>
    <p class="contact-address">Lindenallee 22 <span class="dot">•</span> 41460 Neuss</p>

    <div class="block">
      <h3>Kontakt:</h3>
      <p><span class="label tel">Tel:</span>+49 (0) 2131 / 40 72 118</p>
      <p><span class="label fax">Fax:</span>+49 (0) 2131 / 40 72 119</p>
      <p><span class="label">E-Mail:</span> ra.kaalbayrak@hovenrat-kanzlei.de</p>
      <p><span class="label web">Web:</span>www.hovenrat-kanzlei.de</p>
    </div>

    <div class="block">
      <h3>Öffnungszeiten:</h3>
      <p>Montag bis Freitag</p>
      <p>8:30 Uhr bis 13:00 Uhr</p>
      <p>und 14:00 Uhr bis 17.00 Uhr</p>
    </div>

    <div class="block">
      <h3>Bankverbindung:</h3>
      <p>Kerem Albayrak</p>
      <p>IBAN: DEXX XXXX XXXX XXXX XXXX X</p>
      <p>BIC: XXXXXXXX</p>
      <p>Rheinische Handelsbank</p>
    </div>
  </aside>

  <div class="fold-mark fold-top"></div>
  <div class="fold-mark fold-punch"></div>
  <div class="fold-mark fold-bottom"></div>

  <footer>
    <div class="page-number">-1-</div>
    <div class="footer-mark"></div>
    <div class="footer-name">Halls Of Falcons</div>
    <div class="footer-sub">ANWALTSKOOPERATION</div>
  </footer>

  <div class="bottom-band"></div>
</main>
</body>
</html>
```